依頼詳細
全体のイメージは、キャッチとサブキャッチをメインに講義の内容がわかり易く
セミナーへ来たくなるような興味を惹く、斬新なデザインでお願いします。
注意:講演タイトルや日時を大きく協調される方が多いですが、それは避けてください。
また、イメージとして、協会や会社のHPを記載しておきますので参考にしてください。
・一般社団法人蒼岳地層調査会  https://kvrt-example.or.jp/
・株式会社R-VANTLO  https://rvantlo-example.co.jp/
以前に作っていただいたサンプルチラシがありますが、あまりにも普通なデザインでしたので、悪い事例として添付しておきます。こんなデザインは避けてください。(PPTデータ)
講師の写真データもPPTに入っています。

講師
浦辺 直孝 ※写真入
蒼洋材料技術機構 主幹研究員/博士(工学)
複層素材耐久分析部門 兼 湾岸フロンティア計測センター 主幹研究員
2017年4月9日TVRドキュメント「森の湖 あの町はどこへ?~消えゆく“水辺の記憶”~」新聞・雑誌等掲載多数
講演タイトル「地震大国に必要とされるハイブリット微動探査の将来性」

宮下 航  ※写真入
株式会社Tk’s空間計画 代表取締役社長 「匠研舎」塾長
一級建築士、一級構造建築士 専門は木造構造建築物の構造設計・構造計算
工務店を経て、2006年5月㈱Tk‘s空間計画を設立、2010年1月「匠研舎」を設立し、木質構造に関するセミナーや構造計算技術者育成を行っている。現在は「匠研舎」の講座をweb化した「匠研舎チャンネル」、Cliporaにて情報発信中。著書に「すっきり学べる!石積み読本」がある
講演タイトル「地盤の揺れやすさを知った家づくりの重要性」

主催
株式会社R-VANTLO
〒471-0835愛知県名古屋市中区桜庭二丁目8番4号‐705号
URL:https://rvantlo-example.co.jp/

協賛
・一般社団法人蒼岳地層調査会 ・一般社団法人ソルベン ・株式会社タカミネ

問い合わせ
株式会社R-VANTLO 担当 村瀬 080-2938-6074
murase-hideaki@rvantlo-example.co.jp

記載項目
以下の『』内の文章を入れて下さい。
・セミナータイトル『最新工務店戦略・地盤の揺れやすさを知って地震に備えた家づくり』
・キャッチコピー『揺れにくい地盤には 価値がある』
・サブキャッチ『地盤の揺れやすさは、 今までの地盤測定方法では 計測出来ませんでした』
・セミナースケジュール
『日時:6月23日(水) 14:00~16:00(受付開始13:30)
場所:刈谷市中央障害学習センター5階(501~503)
定員:50名
同時 LIVE配信での開催(Meetrio利用)』
・『来場者特典:当日会場に来ていただいた方には、初回調査を来場者特別価格にてご提供』
・講師名 写真入り 略歴 講演タイトルをそれぞれ入れて下さい。(依頼詳細参照)
・主催、協賛、問い合わせも入れて下さい。(依頼詳細参照)
※参加申込み欄の作成をお願いします。
『会社名、住所、参加者名、部署名、役職名、TEL、FAX、E-mail、参加人数、参加方法、現地かWEB』
・『WEBでご参加の場合はE-mailを必ずご記入下さい。』
・『会場入場前にご名刺を1枚頂戴いたしますのでご準備ください。』

サイズ
A4
ページ数
片面
希望イメージ
シンプル 複雑
単色 カラフル
暗い 明るい
日常 高級
遊び心 厳粛
未来的 伝統的
女性的 男性的
希望する色
設定なし
納品ファイル
• 高解像度JPG (.jpg)
• イラストレーター形式 (.ai)
• フォトショップ形式 (.psd)
補足説明
.ai形式はオリジナル&アウトライン化したものをください。イラストレーターのバージョンをCS6でお願いします。
.pdf(高解像度)をください。
チラシ内で使った画像を別途ください。
申込方法にWEB(Formlaneフォーム)も追加して下さい。
QRコードを添付しましたので宜しくお願い致します。
■ 選んだ理由

選ばせていただいた理由は、他の提案に比べて、圧倒的にインパクトでした。今回は折込チラシではなく、手渡しがメインのため、デザインや構図が一般的なものは外させていただきました。また、こちらの要望をよく把握されていない方もいらっしゃったようで、そのような提案も外させていただきました。
当選させていただいた提案は、使用する文字数が多い中、全体的に上手くまとめていただきまして、それでいて文字もしっかり目に入ってきて、こちらの要望にしっかりと応えてくれました、とても満足のいくものでした。

■ 提案者全員のお礼・コメント

コンペに応募していただいた皆様、本当にありがとうございました。当選された方以外にも、良い出来の提案が複数あり、最後まで悩み、当選と次点を選ばせていただきました。連絡が遅くなり申し訳ありませんでした。今回はこのような結果にさせていただきました。今後も定期的に依頼することがありますので、次回はまた、提案していただけると有難いです。今後とも宜しくお願い致します。

```html
<!DOCTYPE html>
<html lang="ja">
<head>
<meta charset="utf-8">
<title>揺れにくい地盤には価値がある セミナー</title>
<link rel="stylesheet" href="https://fonts.googleapis.com/css2?family=Noto+Sans+JP:wght@400;500;700;900&display=swap">
<style>
:root{
  --red:#e5332a;
  --navy:#1c2a57;
  --blue:#2a6db3;
  --sky:#e9f1f9;
  --yellow:#fff4b8;
  --ink:#222;
  --line:#9aa6b5;
  --paper:#ffffff;
}
*{box-sizing:border-box;margin:0;padding:0}
html,body{width:842px;height:1200px;overflow:hidden;background:#fff}
body{font-family:"Noto Sans JP",sans-serif;color:var(--ink)}
.flyer{position:relative;width:842px;height:1200px;background:var(--paper);overflow:hidden}

.hero-photo{position:absolute;left:380px;top:0;width:462px;height:430px;
  background:linear-gradient(160deg,#eef2f6 0%,#cfd8e2 45%,#9aa9b8 80%,#7b8a99 100%)}
.device-tag{position:absolute;left:640px;top:356px;background:#fff;border:2px solid var(--navy);
  color:var(--navy);font-weight:700;font-size:15px;padding:3px 10px;border-radius:4px;display:flex;align-items:center;gap:6px}
.device-tag i{width:10px;height:10px;background:var(--navy);border-radius:50%;display:block}

.series{position:absolute;left:32px;top:18px;font-weight:900;font-size:24px;line-height:1.35;color:var(--navy)}
.catch{position:absolute;left:28px;top:98px;font-weight:900;color:var(--red);font-size:80px;line-height:88px;
  letter-spacing:-2px;text-shadow:0 0 6px #fff,0 0 2px #fff}
.catch span{display:block}
.catch .indent{padding-left:56px}
.sub{position:absolute;left:32px;top:372px;font-weight:700;font-size:18px;line-height:1.5;color:var(--navy)}

.date-block{position:absolute;left:28px;top:440px;display:flex;align-items:center;gap:14px;color:var(--navy)}
.date{font-weight:900;font-size:96px;line-height:1;letter-spacing:-4px}
.date small{font-size:64px;letter-spacing:0}
.weekday{width:50px;height:50px;border-radius:50%;background:var(--navy);color:#fff;font-weight:900;font-size:28px;
  display:flex;align-items:center;justify-content:center}
.time{font-weight:900;line-height:1.2}
.time b{display:block;font-size:32px}
.time span{font-size:19px}
.time em{font-style:normal;display:block;font-size:25px;margin-top:2px}
.venue{position:absolute;left:28px;top:546px;width:560px;background:var(--navy);color:#fff;font-weight:700;font-size:18px;padding:4px 12px}
.live{position:absolute;left:28px;top:580px;width:560px;background:var(--yellow);color:var(--red);font-weight:900;font-size:19px;padding:2px 12px}

.bonus{position:absolute;left:604px;top:444px;width:212px;height:166px;border:3px solid var(--red);background:#fff;text-align:center;padding:8px 10px}
.bonus h3{background:var(--red);color:#fff;font-size:23px;font-weight:900;padding:2px 0;margin:-2px -4px 8px}
.bonus p{font-size:14px;font-weight:700;line-height:1.55;color:var(--navy)}
.bonus p strong{color:var(--red);font-size:16px;font-weight:900;background:var(--yellow)}

.speakers{position:absolute;left:0;top:622px;width:842px;height:216px;background:var(--sky);display:flex;gap:14px;padding:10px 20px}
.speaker{flex:1;background:#fff;border-radius:6px;padding:8px 10px;position:relative;display:flex;gap:8px}
.speaker .body{flex:1;min-width:0}
.talk{font-size:12px;font-weight:700;color:var(--blue);line-height:1.35}
.talk strong{display:block;font-size:14px;color:var(--navy)}
.name{margin-top:4px;font-size:12px;font-weight:700;color:var(--navy)}
.name b{font-size:20px;font-weight:900;margin-left:6px}
.bio{margin-top:3px;font-size:9px;line-height:1.4;color:#444}
.portrait{width:92px;height:120px;flex:none;border-radius:4px;background:linear-gradient(180deg,#d9dde3,#8f99a6)}

.apply{position:absolute;left:20px;top:848px;width:802px}
.apply h2{background:var(--blue);color:#fff;font-size:16px;font-weight:700;padding:2px 12px;display:inline-block}
.ways{display:flex;align-items:center;gap:14px;margin:4px 0 2px;color:var(--navy);font-weight:900}
.ways .fax{font-size:18px}
.ways .num{font-size:25px;letter-spacing:1px}
.ways .web{font-size:15px;color:var(--blue);display:flex;align-items:center;gap:4px}
.notes{font-size:10px;color:#444;margin-bottom:4px}
.form{width:100%;border-collapse:collapse;font-size:11px}
.form th,.form td{border:1px solid var(--line);height:20px;padding:0 6px;text-align:left}
.form th{background:var(--sky);width:88px;font-weight:700;color:var(--navy)}
.form .kana th,.form .kana td{height:14px;font-size:9px;font-weight:500}
.check{display:inline-block;width:10px;height:10px;border:1px solid var(--ink);margin:0 3px 0 8px;vertical-align:-1px}

.footer{position:absolute;left:0;top:1112px;width:842px;height:88px;background:var(--navy);color:#fff;display:flex;align-items:center;justify-content:space-between;padding:0 20px}
.host{font-size:13px;font-weight:700}
.host b{font-size:22px;font-weight:900;margin-left:4px}
.host p{font-size:9.5px;font-weight:400;margin-top:3px;opacity:.9}
.contact{font-size:10px;line-height:1.5;text-align:right}
.contact .tel{font-size:20px;font-weight:900;display:flex;align-items:center;gap:6px;justify-content:flex-end}
</style>
</head>
<body>
<div class="flyer">
  <div class="hero-photo" role="img" aria-label="住宅模型と地盤を虫眼鏡でのぞき込む写真、微動探査機の写真"></div>
  <div class="device-tag"><i></i>微動探査機</div>

  <p class="series">最新工務店戦略・地盤の揺れやすさを<br>知って地震に備えた家づくり</p>
  <h1 class="catch"><span>揺れにくい</span><span class="indent">地盤には</span><span>価値がある</span></h1>
  <p class="sub">地盤の揺れやすさは、今までの地盤測定方法では<br>計測出来ませんでした</p>

  <div class="date-block">
    <div class="date">6<small>/</small>23</div>
    <div class="weekday">水</div>
    <div class="time"><b>14:00~16:00</b><span>(受付開始13:30)</span><em>定員:50名</em></div>
  </div>
  <p class="venue">場所:刈谷市北部市民交流ホール5階(501~503)</p>
  <p class="live">同時にLIVE配信でも開催(Meetrio利用)</p>

  <div class="bonus">
    <h3>来場者特典</h3>
    <p>当日会場に来ていただいた方には、初回調査を<br><strong>来場者特別価格</strong><br>にてご提供!</p>
  </div>

  <section class="speakers">
    <article class="speaker">
      <div class="body">
        <p class="talk">講演<strong>地震大国に必要とされるハイブリット微動探査の将来性</strong></p>
        <p class="name">講師<b>浦辺 直孝</b></p>
        <p class="bio">蒼洋材料技術機構 主幹研究員/博士(工学)<br>複層素材耐久分析部門 兼 湾岸フロンティア計測センター 主幹研究員<br>2017年4月9日TVRドキュメント「森の湖 あの町はどこへ?~消えゆく“水辺の記憶”~」新聞・雑誌等掲載多数</p>
      </div>
      <div class="portrait" role="img" aria-label="講師 浦辺直孝の写真"></div>
    </article>
    <article class="speaker">
      <div class="body">
        <p class="talk">講演<strong>地盤の揺れやすさを知った家づくりの重要性</strong></p>
        <p class="name">講師<b>宮下 航</b></p>
        <p class="bio">株式会社Tk’s空間計画 代表取締役社長 「匠研舎」塾長<br>一級建築士、一級構造建築士 専門は木造構造建築物の構造設計・構造計算。2006年5月㈱Tk‘s空間計画を設立、2010年1月「匠研舎」を設立。現在は「匠研舎チャンネル」、Cliporaにて情報発信中。著書に「すっきり学べる!石積み読本」</p>
      </div>
      <div class="portrait" role="img" aria-label="講師 宮下航の写真"></div>
    </article>
  </section>

  <section class="apply">
    <h2>お申し込み方法</h2>
    <div class="ways">
      <span class="fax">FAX でお申込み</span>
      <svg width="24" height="24" viewBox="0 0 24 24" aria-hidden="true"><path fill="#1c2a57" d="M6.6 10.8a15 15 0 0 0 6.6 6.6l2.2-2.2a1 1 0 0 1 1-.25 11.4 11.4 0 0 0 3.6.57 1 1 0 0 1 1 1V20a1 1 0 0 1-1 1A17 17 0 0 1 3 4a1 1 0 0 1 1-1h3.5a1 1 0 0 1 1 1c0 1.25.2 2.45.57 3.57a1 1 0 0 1-.25 1z"/></svg>
      <span class="num">000-000-0000</span>
      <span class="web">スマホでお申込み(Formlaneフォーム)
        <svg width="16" height="16" viewBox="0 0 16 16" aria-hidden="true"><path d="M3 8h9M8 4l4 4-4 4" stroke="#2a6db3" stroke-width="2" fill="none"/></svg></span>
    </div>
    <p class="notes">※ WEBでご参加の場合はE-mailを必ずご記入下さい。 ※ 会場入場前にご名刺を1枚頂戴いたしますのでご準備ください。</p>
    <table class="form">
      <tr class="kana"><th>フリガナ</th><td colspan="3"></td></tr>
      <tr><th>会社名</th><td colspan="3"></td></tr>
      <tr><th>住所</th><td colspan="3">〒</td></tr>
      <tr class="kana"><th>フリガナ</th><td></td><th>参加人数</th><td></td></tr>
      <tr><th>参加者名</th><td></td><th>参加方法</th><td><span class="check"></span>現地<span class="check"></span>WEB</td></tr>
      <tr><th>部署名</th><td></td><th>役職名</th><td></td></tr>
      <tr><th>TEL</th><td></td><th>FAX</th><td></td></tr>
      <tr><th>E-mail</th><td colspan="3"></td></tr>
    </table>
  </section>

  <footer class="footer">
    <div class="host">主催<b>株式会社R-VANTLO</b>
      <p>〒471-0835愛知県名古屋市中区桜庭二丁目8番4号‐705号 URL:https://rvantlo-example.co.jp/<br>協賛:一般社団法人蒼岳地層調査会・一般社団法人ソルベン・株式会社タカミネ</p>
    </div>
    <div class="contact">お問い合わせ 株式会社R-VANTLO 担当 村瀬
      <div class="tel"><svg width="18" height="18" viewBox="0 0 24 24" aria-hidden="true"><path fill="#fff" d="M6.6 10.8a15 15 0 0 0 6.6 6.6l2.2-2.2a1 1 0 0 1 1-.25 11.4 11.4 0 0 0 3.6.57 1 1 0 0 1 1 1V20a1 1 0 0 1-1 1A17 17 0 0 1 3 4a1 1 0 0 1 1-1h3.5a1 1 0 0 1 1 1c0 1.25.2 2.45.57 3.57a1 1 0 0 1-.25 1z"/></svg>080-2938-6074</div>
      murase-hideaki@rvantlo-example.co.jp
    </div>
  </footer>
</div>
</body>
</html>
```